A.I. Software PowerPoint Presentation

We need a PowerPoint presentation design for our artificial intelligence product vxMender.

We've attached our current PowerPoint to use as a base. This presentation is used to introduce and describe what the product is, how it works, why you need it, what makes it better than other solutions, and how to implement it.

We would like the PowerPoint design to be more professional-looking as we present to executives and CIOs of banks, government, and other large corporations. We are a tech startup and would like the design to convey the feel of innovation and high-tech, but also trustworthy, reputable, and capable, for the more conservative audiences.

The PowerPoint should have minimal use of animation (animate only if necessary). It should be modern and clean and not too busy.

We appreciate design work on all of the following: slide backgrounds, title slide, fonts, pictures used in the slides, layout, charts, graphics, comparison versus, etc. If you have any ideas for the slide contents, please also provide any suggestions/recommendations.

I've also attached our vxMender logo if that is needed, as well as our brochure.

We look forward to your submissions!

EDIT:
I would like to add that we are using PowerPoint 2010 on a PC (.pptx file), and that the slides should be in 16:9 mainly but also with 4:3 version (if possible cut off the sides and squish in the content a little, no need to make a new set of slides) as sometimes we cannot control whose projector we are presenting on. Thanks

Target Market(s)

Enterprise clients, multi-national corporations,
banks, airlines, telecommunications, government

Industry/Entity Type

Software

Font styles to use
Serif
Sans Serif

Colors

Designer to choose colors to be used in the design.

Requirements
Nice to have
• Professional, clean-look, modern design
Should not have
• Should not look cheesy (i.e. tons of stock photos, business cliche pictures)
• Should not look over-done/over-the-top
• Should not look outdated

```html
<!DOCTYPE html>
<html lang="en">
<head>
<meta charset="utf-8">
<title>vxMender – Presentation Template Overview</title>
<link href="https://fonts.googleapis.com/css2?family=Open+Sans:wght@300;400;600;700&display=swap" rel="stylesheet">
<style>
:root{
  --blue:#1ba9e1;
  --blue-d:#0a86c2;
  --blue-l:#5cc6ef;
  --navy:#0c2237;
  --navy-2:#16395a;
  --ink:#2b3a4a;
  --gray:#8793a0;
  --line:#d7dde3;
  --pale:#e7f4fb;
  --bg:#e9ecef;
  --white:#ffffff;
}
*{box-sizing:border-box}
html,body{margin:0;padding:0}
body{width:1200px;height:3328px;overflow:hidden;background:var(--bg);font-family:'Open Sans',sans-serif;color:var(--ink)}
.deck{width:1200px;height:3328px;padding:6px;display:grid;grid-template-columns:repeat(3,1fr);grid-template-rows:repeat(15,1fr);gap:8px}
.slide{position:relative;overflow:hidden;background:var(--white)}
.slide.blue{background:linear-gradient(135deg,var(--blue-l),var(--blue) 45%,var(--blue-d));color:var(--white)}
.slide.dark{background:var(--navy);color:var(--white)}
.slide.tpl::after{content:"";position:absolute;right:0;bottom:0;border-left:16px solid transparent;border-bottom:16px solid var(--blue)}
.abs{position:absolute}
.title{position:absolute;left:16px;top:12px;margin:0;font-size:12px;font-weight:600;color:var(--blue-d)}
.title::after{content:"";display:block;width:22px;height:2px;margin-top:4px;background:var(--blue)}
.brand-sm{position:absolute;right:16px;top:12px;font-size:8px;font-weight:700;color:var(--blue-d);display:flex;align-items:center;gap:3px}
.brand-sm i,.logo i{display:inline-block;border-radius:50%;background:currentColor}
.brand-sm i{width:7px;height:7px}
.logo{display:flex;align-items:center;gap:8px;font-weight:700;color:var(--white);letter-spacing:.5px}
.logo i{width:26px;height:26px}
.center{position:absolute;inset:0;display:flex;flex-direction:column;align-items:center;justify-content:center;text-align:center}
.p{margin:0;font-size:6px;line-height:1.5;color:var(--gray)}
.p.w{color:rgba(255,255,255,.85)}
.h{margin:0 0 3px;font-size:8px;font-weight:600;color:var(--ink)}
.h.b{color:var(--blue-d)}
.h.w{color:var(--white)}
.big{font-size:16px;font-weight:600;line-height:1.2;margin:0}
.ph{position:absolute}
.ph-sky{background:linear-gradient(135deg,#7fd3f3,#1b9bd5 60%,#0a6da3)}
.ph-deep{background:linear-gradient(135deg,#0f3556,#0a1b2e 70%)}
.ph-steel{background:linear-gradient(135deg,#b9c6d1,#6d8396)}
.ph-mist{background:linear-gradient(135deg,#dfe8ee,#aabdcb)}
.ph-cyan{background:linear-gradient(160deg,#2fb6e8,#0b4f85)}
.ph-green{background:linear-gradient(180deg,#0c2a1c,#2e9d55)}
.ic{display:inline-block;width:16px;height:16px;border-radius:50%;background:var(--blue);flex:none}
.ic.o{background:none;border:2px solid var(--blue)}
.row{display:flex;gap:6px;align-items:flex-start}
.col{flex:1}
.bul{margin:0;padding:0;list-style:none}
.bul li{font-size:6px;color:var(--gray);line-height:1.6;padding-left:8px;position:relative}
.bul li::before{content:"";position:absolute;left:0;top:3px;width:4px;height:4px;background:var(--blue);border-radius:50%}
.box{background:var(--pale);border-top:2px solid var(--blue);padding:5px}
.chip{position:absolute;background:var(--blue);color:var(--white);font-size:9px;font-weight:600;padding:4px 10px}
.pct{font-size:7px;font-weight:700;fill:var(--ink)}
</style>
</head>
<body>
<main class="deck">

<!-- Row 1 -->
<section class="slide blue">
  <div class="ph ph-cyan" style="inset:0" role="img" aria-label="Blue backdrop of flowing digital code"></div>
  <div class="center"><div class="logo" style="font-size:30px"><i></i>vxMender</div></div>
</section>

<section class="slide tpl">
  <svg class="abs" style="left:0;top:0" width="200" height="214" viewBox="0 0 200 214">
    <polygon points="0,0 150,0 60,214 0,214" fill="#0c2237"/>
    <polygon points="120,0 190,0 100,214 30,214" fill="#1ba9e1" opacity=".9"/>
    <polygon points="150,0 175,0 85,214 60,214" fill="#ffffff" opacity=".25"/>
  </svg>
  <div class="abs" style="left:210px;top:84px">
    <p class="big" style="color:var(--blue-d)">Your Title Goes Here</p>
    <p class="p" style="font-size:8px;margin-top:4px">Your Subtitle Goes Here</p>
  </div>
</section>

<section class="slide blue">
  <div class="center"><div class="logo" style="font-size:26px"><i></i>vxMender</div></div>
</section>

<!-- Row 2 -->
<section class="slide tpl">
  <h2 class="title">Our Agenda</h2>
  <div class="brand-sm"><i></i>vxMender</div>
  <div class="abs" style="left:20px;top:52px;right:20px;display:grid;grid-template-columns:1fr 1fr;gap:14px 24px">
    <div class="row"><span class="ic"></span><div><p class="h">Introduction</p><p class="p">Who we are and why.</p></div></div>
    <div class="row"><span class="ic"></span><div><p class="h">The Product</p><p class="p">What the platform does.</p></div></div>
    <div class="row"><span class="ic"></span><div><p class="h">How It Works</p><p class="p">Core engine explained.</p></div></div>
    <div class="row"><span class="ic"></span><div><p class="h">Why You Need It</p><p class="p">Costs and outcomes.</p></div></div>
    <div class="row"><span class="ic"></span><div><p class="h">Comparison</p><p class="p">Versus other solutions.</p></div></div>
    <div class="row"><span class="ic"></span><div><p class="h">Implementation</p><p class="p">Steps to go live.</p></div></div>
  </div>
</section>

<section class="slide dark">
  <div class="ph ph-deep" style="inset:0" role="img" aria-label="Night view of the earth from orbit"></div>
  <div class="abs" style="left:200px;top:40px;width:170px">
    <p class="h w" style="font-size:10px">Connected Worldwide</p>
    <p class="p w">Our platform serves contact centers across many regions with secure and scalable cloud services.</p>
    <p class="p w" style="margin-top:6px">Built for banks, airlines and public agencies.</p>
  </div>
</section>

<section class="slide blue">
  <div class="ph ph-steel" style="right:0;top:0;bottom:0;width:48%;opacity:.6" role="img" aria-label="Portrait photo with digital overlay"></div>
  <div class="abs" style="left:18px;top:60px;width:170px">
    <p class="big">Innovation you can trust</p>
    <p class="p w" style="margin-top:6px">Artificial intelligence that helps teams resolve every customer request faster.</p>
  </div>
</section>

<!-- Row 3 -->
<section class="slide blue">
  <div class="abs" style="left:30px;top:70px;width:56px;height:56px;border-radius:50%;background:var(--white);display:flex;align-items:center;justify-content:center">
    <svg width="24" height="20" viewBox="0 0 24 20"><path d="M0 20V11C0 4 4 1 9 0v4C6 5 5 7 5 10h4v10zM14 20V11c0-7 4-10 9-11v4c-3 1-4 3-4 6h4v10z" fill="#1ba9e1"/></svg>
  </div>
  <div class="abs" style="left:104px;top:74px;width:250px">
    <p style="margin:0;font-size:10px;line-height:1.45">A smart assistant is the fastest way to bring calm, clear answers to every customer.</p>
  </div>
</section>

<section class="slide tpl">
  <h2 class="title">Our Vision &amp; Mission</h2>
  <div class="ph ph-deep" style="left:16px;right:16px;top:42px;height:72px" role="img" aria-label="World map in dark blue tones"></div>
  <div class="abs row" style="left:16px;right:16px;top:124px;gap:16px">
    <div class="col"><p class="h b">Vision</p><p class="p">Every customer conversation made effortless by intelligent software.</p></div>
    <div class="col"><p class="h b">Mission</p><p class="p">Deliver reliable automation that large organisations can trust.</p></div>
  </div>
</section>

<section class="slide">
  <div class="abs" style="inset:14px 14px auto;display:grid;grid-template-columns:repeat(4,1fr);gap:10px">
    <div style="height:34px;background:var(--line)"></div><div style="height:34px;background:var(--line)"></div><div style="height:34px;background:var(--line)"></div><div style="height:34px;background:var(--line)"></div>
  </div>
  <div class="abs" style="left:0;right:0;top:90px;height:36px;background:var(--blue);color:var(--white);display:flex;align-items:center;justify-content:center;font-size:13px;font-weight:600">Our Previous work</div>
  <div class="abs" style="inset:auto 14px 14px;display:grid;grid-template-columns:repeat(4,1fr);gap:10px">
    <div style="height:34px;background:var(--line)"></div><div style="height:34px;background:var(--line)"></div><div style="height:34px;background:var(--line)"></div><div style="height:34px;background:var(--line)"></div>
  </div>
</section>

<!-- Row 4 -->
<section class="slide tpl">
  <h2 class="title">Your Title Goes Here</h2>
  <div class="abs" style="left:16px;top:50px;width:160px">
    <p class="p">Our assistant understands intent, routes calls and learns from every interaction to improve service.</p>
    <ul class="bul" style="margin-top:8px"><li>Faster resolution</li><li>Lower handling cost</li><li>Happier customers</li></ul>
  </div>
  <div class="ph ph-mist" style="right:16px;top:40px;width:180px;height:150px" role="img" aria-label="Photo of a modern office workspace"></div>
</section>

<section class="slide tpl">
  <h2 class="title">Portfolio Area</h2>
  <div class="abs" style="left:16px;top:50px;width:150px">
    <p class="h">Selected Projects</p>
    <p class="p">Deployments for finance, travel and telecom clients around the world.</p>
  </div>
  <div class="abs" style="right:16px;top:40px;width:190px;height:150px;display:grid;grid-template-columns:1fr 1fr;gap:4px">
    <div class="ph ph-deep" style="position:relative" role="img" aria-label="Project photo of a data center"></div>
    <div class="ph ph-cyan" style="position:relative" role="img" aria-label="Project photo of city lights"></div>
    <div class="ph ph-steel" style="position:relative" role="img" aria-label="Project photo of a call center"></div>
    <div class="ph ph-sky" style="position:relative" role="img" aria-label="Project photo of network cables"></div>
  </div>
</section>

<section class="slide">
  <div class="ph ph-steel" style="right:0;top:0;bottom:0;width:55%" role="img" aria-label="Portrait photo in cool grey tones"></div>
  <div class="abs" style="left:18px;top:60px;width:150px">
    <p style="margin:0;font-size:11px;font-weight:600;color:var(--blue-d);line-height:1.35">The future of customer service starts with one smart step.</p>
    <p class="p" style="margin-top:6px">Automation with a human touch.</p>
  </div>
</section>

<!-- Row 5 -->
<section class="slide tpl">
  <h2 class="title">Our Differences</h2>
  <div class="ph ph-mist" style="left:120px;top:44px;width:150px;height:80px;border:3px solid var(--blue)" role="img" aria-label="Photo of a modern glass building interior"></div>
  <div class="abs row" style="left:16px;right:16px;top:138px;gap:14px">
    <div class="col"><p class="p">Trained on real enterprise conversations.</p></div>
    <div class="col"><p class="p">Deploys in weeks, not months.</p></div>
    <div class="col"><p class="p">Security built for regulated industries.</p></div>
  </div>
</section>

<section class="slide tpl">
  <h2 class="title">Two Column Description</h2>
  <div class="abs row" style="left:16px;right:16px;top:52px;gap:18px">
    <div class="col"><p class="h b">Cloud Based</p><p class="p">Runs fully in the cloud with no local servers to maintain. Scale up during peak season and down again with ease.</p></div>
    <div class="col"><p class="h b">Always Learning</p><p class="p">Models improve over time from resolved cases, giving your agents better suggestions every single week.</p></div>
  </div>
</section>

<section class="slide">
  <div class="ph ph-mist" style="inset:0" role="img" aria-label="Photo of a coffee cup on a desk"></div>
  <div class="abs" style="left:110px;top:26px;width:170px;height:70px;background:var(--white);display:flex;flex-direction:column;align-items:center;justify-content:center">
    <p style="margin:0;font-size:12px;font-weight:700;letter-spacing:2px;color:var(--navy)">COFFEE BREAK</p>
    <p class="p">Back in fifteen minutes</p>
  </div>
  <div class="brand-sm" style="top:auto;bottom:20px;right:50%;transform:translateX(50%)"><i></i>vxMender</div>
</section>

<!-- Row 6 -->
<section class="slide tpl">
  <h2 class="title">Three Column Description</h2>
  <div class="abs row" style="left:16px;right:16px;top:56px;gap:14px;text-align:center">
    <div class="col"><span class="ic" style="width:26px;height:26px"></span><p class="h" style="margin-top:6px">Listen</p><p class="p">Captures every request in real time.</p></div>
    <div class="col"><span class="ic" style="width:26px;height:26px"></span><p class="h" style="margin-top:6px">Understand</p><p class="p">Detects intent and customer mood.</p></div>
    <div class="col"><span class="ic" style="width:26px;height:26px"></span><p class="h" style="margin-top:6px">Resolve</p><p class="p">Suggests the best next action.</p></div>
  </div>
</section>

<section class="slide dark">
  <div class="ph ph-deep" style="inset:0" role="img" aria-label="Dark high tech corridor with blue light"></div>
  <div class="abs" style="left:210px;top:60px;width:150px;padding:10px;background:rgba(27,169,225,.85)">
    <p class="h w" style="font-size:11px">Your Title Goes Here</p>
    <p class="p w">Short supporting line of text.</p>
  </div>
</section>

<section class="slide tpl">
  <h2 class="title">Your Title Goes Here</h2>
  <div class="abs" style="left:16px;top:50px;width:170px">
    <p class="p">Reduce queue times and free your agents to handle complex issues while the assistant covers routine questions.</p>
  </div>
  <div class="ph ph-sky" style="right:0;top:40px;width:170px;height:140px" role="img" aria-label="Photo of a person using a tablet"></div>
</section>

<!-- Row 7 -->
<section class="slide tpl">
  <h2 class="title">Four Boxes with Paragraph</h2>
  <div class="abs" style="left:16px;right:16px;top:46px;display:grid;grid-template-columns:1fr 1fr;gap:10px 16px">
    <div class="row"><span class="ic"></span><div><p class="h">Speed</p><p class="p">Answers in under a second.</p></div></div>
    <div class="row"><span class="ic"></span><div><p class="h">Accuracy</p><p class="p">High intent match rates.</p></div></div>
    <div class="row"><span class="ic"></span><div><p class="h">Security</p><p class="p">Encrypted end to end.</p></div></div>
    <div class="row"><span class="ic"></span><div><p class="h">Support</p><p class="p">Help whenever you need.</p></div></div>
  </div>
</section>

<section class="slide tpl">
  <h2 class="title">Your Title</h2>
  <div class="abs" style="left:16px;top:60px;width:100px"><p class="p">Our engine blends language models with business rules.</p></div>
  <div class="ph ph-steel" style="left:135px;top:30px;width:110px;height:175px;border-radius:50px 50px 0 0" role="img" aria-label="Illustration of a silver robot figure"></div>
  <div class="abs" style="right:18px;top:60px;width:100px"><p class="p">It fits into the tools your team already uses.</p></div>
</section>

<section class="slide tpl">
  <h2 class="title">Text &amp; Bullet Area</h2>
  <div class="abs row" style="left:16px;right:16px;top:52px;gap:18px">
    <div class="col"><p class="p">A clear summary of the benefits that matter most to your operations team.</p></div>
    <div class="col"><ul class="bul"><li>Fewer repeat calls</li><li>Shorter wait times</li><li>Consistent answers</li><li>Detailed reporting</li></ul></div>
  </div>
</section>

<!-- Row 8 -->
<section class="slide blue">
  <div class="ph ph-cyan" style="inset:0" role="img" aria-label="Blue tinted photo of steel structure"></div>
  <div class="abs" style="left:18px;bottom:26px">
    <p class="big">Your Title Goes Here</p>
    <p class="p w">Your subtitle</p>
  </div>
</section>

<section class="slide tpl">
  <h2 class="title">Paragraph with Three Bullet</h2>
  <div class="abs" style="left:16px;top:48px;width:160px"><p class="p">Three simple reasons why leading enterprises choose our assistant for customer care.</p></div>
  <div class="abs" style="right:20px;top:44px;width:170px;display:flex;flex-direction:column;gap:12px">
    <div class="row"><span class="ic o"></span><p class="p">Proven at large scale.</p></div>
    <div class="row"><span class="ic o"></span><p class="p">Simple monthly pricing.</p></div>
    <div class="row"><span class="ic o"></span><p class="p">Local expert support.</p></div>
  </div>
</section>

<section class="slide tpl">
  <h2 class="title">Global Experience</h2>
  <div class="ph" style="left:40px;top:42px;width:300px;height:140px;background:linear-gradient(135deg,#c9d3db,#9fb0bd)" role="img" aria-label="World map in grey with office locations"></div>
  <span class="abs ic" style="left:110px;top:90px;width:8px;height:8px"></span>
  <span class="abs ic" style="left:200px;top:80px;width:8px;height:8px"></span>
  <span class="abs ic" style="left:280px;top:120px;width:8px;height:8px"></span>
</section>

<!-- Row 9 -->
<section class="slide tpl">
  <h2 class="title">Global Experience</h2>
  <div class="ph" style="left:16px;top:44px;width:230px;height:140px;background:linear-gradient(135deg,#6cc9ef,#1ba9e1 50%,#0c2237)" role="img" aria-label="Map of the United States with highlighted states"></div>
  <div class="abs" style="right:16px;top:56px;width:110px">
    <p class="h b">12 Regions</p><p class="p">Active deployments in major cities.</p>
  </div>
</section>

<section class="slide tpl">
  <h2 class="title">Multiple Column Area</h2>
  <div class="abs row" style="left:16px;right:16px;top:50px;gap:8px">
    <div class="col box"><p class="h">Step 01</p><p class="p">Discover needs.</p></div>
    <div class="col box"><p class="h">Step 02</p><p class="p">Connect systems.</p></div>
    <div class="col box"><p class="h">Step 03</p><p class="p">Train the model.</p></div>
    <div class="col box"><p class="h">Step 04</p><p class="p">Go live.</p></div>
  </div>
</section>

<section class="slide tpl">
  <h2 class="title">Your Pie Chart Area</h2>
  <svg class="abs" style="left:16px;top:60px" width="358" height="90" viewBox="0 0 358 90">
    <g fill="none" stroke-width="7">
      <circle cx="40" cy="40" r="26" stroke="#d7dde3"/><circle cx="40" cy="40" r="26" stroke="#1ba9e1" stroke-dasharray="122 163" transform="rotate(-90 40 40)"/>
      <circle cx="130" cy="40" r="26" stroke="#d7dde3"/><circle cx="130" cy="40" r="26" stroke="#1ba9e1" stroke-dasharray="90 163" transform="rotate(-90 130 40)"/>
      <circle cx="220" cy="40" r="26" stroke="#d7dde3"/><circle cx="220" cy="40" r="26" stroke="#1ba9e1" stroke-dasharray="65 163" transform="rotate(-90 220 40)"/>
      <circle cx="310" cy="40" r="26" stroke="#d7dde3"/><circle cx="310" cy="40" r="26" stroke="#0c2237" stroke-dasharray="140 163" transform="rotate(-90 310 40)"/>
    </g>
    <text class="pct" x="40" y="43" text-anchor="middle">75%</text><text class="pct" x="130" y="43" text-anchor="middle">55%</text>
    <text class="pct" x="220" y="43" text-anchor="middle">40%</text><text class="pct" x="310" y="43" text-anchor="middle">86%</text>
  </svg>
</section>

<!-- Row 10 -->
<section class="slide tpl">
  <h2 class="title">Your Pie Chart Area</h2>
  <svg class="abs" style="left:16px;top:46px" width="230" height="140" viewBox="0 0 230 140">
    <g fill="none" stroke-width="6">
      <circle cx="30" cy="30" r="20" stroke="#d7dde3"/><circle cx="30" cy="30" r="20" stroke="#1ba9e1" stroke-dasharray="90 126" transform="rotate(-90 30 30)"/>
      <circle cx="30" cy="100" r="20" stroke="#d7dde3"/><circle cx="30" cy="100" r="20" stroke="#0c2237" stroke-dasharray="60 126" transform="rotate(-90 30 100)"/>
      <circle cx="130" cy="30" r="20" stroke="#d7dde3"/><circle cx="130" cy="30" r="20" stroke="#1ba9e1" stroke-dasharray="40 126" transform="rotate(-90 130 30)"/>
      <circle cx="130" cy="100" r="20" stroke="#d7dde3"/><circle cx="130" cy="100" r="20" stroke="#5cc6ef" stroke-dasharray="110 126" transform="rotate(-90 130 100)"/>
    </g>
  </svg>
  <div class="abs" style="right:18px;top:56px;width:110px"><p class="p">Share of tickets resolved automatically by each channel.</p></div>
</section>

<section class="slide tpl">
  <h2 class="title">Your Pie Chart Area</h2>
  <svg class="abs" style="left:30px;top:50px" width="150" height="130" viewBox="0 0 150 130">
    <ellipse cx="75" cy="72" rx="70" ry="40" fill="#0a86c2"/>
    <path d="M75 62 L75 22 A70 40 0 1 1 12 44 Z" fill="#1ba9e1"/>
    <path d="M75 62 L12 44 A70 40 0 0 1 75 22 Z" fill="#0c2237"/>
  </svg>
  <div class="abs" style="right:18px;top:60px;width:120px">
    <p class="h" style="font-size:14px;color:var(--blue-d)">64%</p>
    <p class="p">Calls handled without an agent.</p>
  </div>
</section>

<section class="slide">
  <svg class="abs" style="right:0;top:0" width="210" height="214" viewBox="0 0 210 214"><polygon points="90,0 210,0 210,214 0,214" fill="#1ba9e1"/></svg>
  <div class="abs" style="left:20px;top:84px">
    <div class="brand-sm" style="position:static"><i></i>vxMender</div>
    <p style="margin:4px 0 0;font-size:11px;font-weight:600;color:var(--navy)">Section Divider Page</p>
  </div>
</section>

<!-- Row 11 -->
<section class="slide blue">
  <svg class="abs" style="left:0;top:0" width="390" height="214" viewBox="0 0 390 214"><polygon points="0,0 160,0 250,107 160,214 0,214" fill="#ffffff" opacity=".12"/><polygon points="180,0 220,0 310,107 220,214 180,214 270,107" fill="#ffffff" opacity=".3"/></svg>
  <div class="abs" style="left:24px;top:84px">
    <div class="logo" style="font-size:10px"><i style="width:10px;height:10px"></i>vxMender</div>
    <p style="margin:4px 0 0;font-size:12px;font-weight:600">Section Divider Page</p>
  </div>
</section>

<section class="slide blue">
  <div class="abs" style="left:22px;top:56px;width:230px">
    <p style="margin:0;font-size:17px;font-weight:300;line-height:1.3">vxMender is a cloud-based contact center solution</p>
  </div>
  <div class="logo abs" style="right:22px;bottom:22px;font-size:10px"><i style="width:10px;height:10px"></i>vxMender</div>
</section>

<section class="slide tpl">
  <h2 class="title">Organization Chart</h2>
  <svg class="abs" style="left:40px;top:44px" width="310" height="150" viewBox="0 0 310 150">
    <g stroke="#8793a0" fill="none"><path d="M155 30V50M55 50H255M55 50V70M155 50V70M255 50V70M155 95V110M105 110H205M105 110V122M205 110V122"/></g>
    <rect x="115" y="6" width="80" height="24" fill="#1ba9e1"/>
    <rect x="20" y="70" width="70" height="25" fill="#0c2237"/><rect x="120" y="70" width="70" height="25" fill="#0c2237"/><rect x="220" y="70" width="70" height="25" fill="#0c2237"/>
    <rect x="75" y="122" width="60" height="22" fill="#5cc6ef"/><rect x="175" y="122" width="60" height="22" fill="#5cc6ef"/>
    <g fill="#fff" font-size="7" text-anchor="middle" font-family="Open Sans, sans-serif">
      <text x="155" y="21">CEO</text><text x="55" y="85">Product</text><text x="155" y="85">Engineering</text><text x="255" y="85">Sales</text>
      <text x="105" y="136">AI Team</text><text x="205" y="136">Cloud</text>
    </g>
  </svg>
</section>

<!-- Row 12 -->
<section class="slide tpl">
  <h2 class="title">Market Performance</h2>
  <svg class="abs" style="left:16px;top:44px" width="360" height="150" viewBox="0 0 360 150">
    <g font-size="7" font-family="Open Sans, sans-serif" fill="#8793a0">
      <polygon points="0,0 40,0 48,10 40,20 0,20" fill="#1ba9e1"/><rect x="60" y="6" width="200" height="8" fill="#d7dde3"/><rect x="60" y="6" width="170" height="8" fill="#1ba9e1"/><text x="270" y="13">Banking</text>
      <polygon points="0,28 40,28 48,38 40,48 0,48" fill="#0a86c2"/><rect x="60" y="34" width="200" height="8" fill="#d7dde3"/><rect x="60" y="34" width="140" height="8" fill="#0a86c2"/><text x="270" y="41">Airlines</text>
      <polygon points="0,56 40,56 48,66 40,76 0,76" fill="#0c2237"/><rect x="60" y="62" width="200" height="8" fill="#d7dde3"/><rect x="60" y="62" width="120" height="8" fill="#0c2237"/><text x="270" y="69">Telecom</text>
      <polygon points="0,84 40,84 48,94 40,104 0,104" fill="#1ba9e1"/><rect x="60" y="90" width="200" height="8" fill="#d7dde3"/><rect x="60" y="90" width="95" height="8" fill="#1ba9e1"/><text x="270" y="97">Government</text>
      <polygon points="0,112 40,112 48,122 40,132 0,132" fill="#0a86c2"/><rect x="60" y="118" width="200" height="8" fill="#d7dde3"/><rect x="60" y="118" width="70" height="8" fill="#0a86c2"/><text x="270" y="125">Retail</text>
    </g>
  </svg>
</section>

<section class="slide tpl">
  <h2 class="title">Business Map Analysis</h2>
  <div class="ph ph-steel" style="left:16px;top:42px;width:150px;height:150px" role="img" aria-label="Illustration of a robot figure beside a chart"></div>
  <div class="abs" style="right:18px;top:50px;width:180px">
    <p class="h b">Key Findings</p>
    <ul class="bul"><li>Demand rising in finance</li><li>Strong growth in travel</li><li>New public sector tenders</li></ul>
  </div>
</section>

<section class="slide tpl">
  <h2 class="title">Performance Level</h2>
  <svg class="abs" style="left:40px;top:46px" width="140" height="140" viewBox="0 0 140 140">
    <circle cx="70" cy="70" r="50" fill="none" stroke="#d7dde3" stroke-width="18"/>
    <circle cx="70" cy="70" r="50" fill="none" stroke="#1ba9e1" stroke-width="18" stroke-dasharray="200 314" transform="rotate(-90 70 70)"/>
    <circle cx="70" cy="70" r="50" fill="none" stroke="#0c2237" stroke-width="18" stroke-dasharray="60 314" stroke-dashoffset="-200" transform="rotate(-90 70 70)"/>
    <text x="70" y="75" text-anchor="middle" font-size="14" font-weight="700" fill="#2b3a4a" font-family="Open Sans, sans-serif">82%</text>
  </svg>
  <div class="abs" style="right:22px;top:64px;width:150px"><p class="p">Service level reached within the first three months after launch.</p></div>
</section>

<!-- Row 13 -->
<section class="slide dark">
  <div class="ph ph-deep" style="inset:0" role="img" aria-label="Dark blue photo of glowing server racks"></div>
  <div class="abs" style="left:18px;top:70px;width:160px">
    <p class="h w" style="font-size:11px">Powered by the Cloud</p>
    <p class="p w">Secure hosting with reliable uptime for critical services.</p>
  </div>
</section>

<section class="slide tpl">
  <h2 class="title">Our Website</h2>
  <div class="abs" style="left:16px;top:56px;width:140px"><p class="p">Learn more, book a demo and explore customer stories online.</p></div>
  <svg class="abs" style="right:30px;top:40px" width="170" height="150" viewBox="0 0 170 150">
    <rect x="2" y="2" width="166" height="106" rx="4" fill="#2b3a4a"/>
    <rect x="10" y="10" width="150" height="90" fill="#ffffff"/>
    <rect x="75" y="108" width="20" height="22" fill="#8793a0"/><rect x="50" y="130" width="70" height="6" fill="#8793a0"/>
    <circle cx="52" cy="55" r="6" fill="#1ba9e1"/>
    <text x="64" y="59" font-size="12" font-weight="700" fill="#1ba9e1" font-family="Open Sans, sans-serif">vxMender</text>
  </svg>
</section>

<section class="slide tpl">
  <div class="abs" style="left:16px;top:30px;width:90px">
    <p style="margin:0;font-size:13px;font-weight:600;color:var(--blue-d);line-height:1.25">This is Line Chart Slide</p>
    <p class="p" style="margin-top:6px">Monthly volume trend.</p>
  </div>
  <svg class="abs" style="right:20px;top:36px" width="240" height="150" viewBox="0 0 240 150">
    <g stroke="#d7dde3"><path d="M10 20H235M10 55H235M10 90H235M10 125H235"/></g>
    <polyline points="10,110 50,80 90,95 130,60 170,70 210,35 235,40" fill="none" stroke="#1ba9e1" stroke-width="2"/>
    <polyline points="10,120 50,105 90,110 130,90 170,95 210,75 235,80" fill="none" stroke="#0c2237" stroke-width="2"/>
  </svg>
</section>

<!-- Row 14 -->
<section class="slide tpl">
  <h2 class="title">Stats Detailed</h2>
  <div class="ph ph-green" style="left:16px;top:42px;width:160px;height:150px" role="img" aria-label="Green digital rain of characters on black"></div>
  <div class="abs" style="right:18px;top:50px;width:170px">
    <p class="h b">3.2M calls</p><p class="p">Handled every month by the assistant.</p>
    <p class="h b" style="margin-top:8px">45 seconds</p><p class="p">Average time saved per call.</p>
  </div>
</section>

<section class="slide tpl">
  <h2 class="title">Title and Image / Text</h2>
  <div class="ph ph-sky" style="left:16px;top:42px;width:170px;height:150px" role="img" aria-label="Digital globe with connection lines"></div>
  <div class="abs" style="right:18px;top:54px;width:165px"><p class="p">Connect every channel — voice, chat and email — into one intelligent workflow for your teams.</p></div>
</section>

<section class="slide tpl">
  <h2 class="title" style="color:var(--white)">Three Bullets Area</h2>
  <div class="ph ph-deep" style="left:0;right:0;top:0;height:80px;z-index:0" role="img" aria-label="Dark blue photo of a city at night"></div>
  <h2 class="title" style="color:var(--white);z-index:1">Three Bullets Area</h2>
  <div class="abs row" style="left:16px;right:16px;top:100px;gap:14px">
    <div class="col"><p class="h b">Plan</p><p class="p">Set goals together.</p></div>
    <div class="col"><p class="h b">Build</p><p class="p">Integrate and test.</p></div>
    <div class="col"><p class="h b">Grow</p><p class="p">Measure and improve.</p></div>
  </div>
</section>

<!-- Row 15 -->
<section class="slide tpl">
  <h2 class="title">Our Team</h2>
  <div class="abs" style="left:16px;right:16px;top:46px;display:grid;grid-template-columns:repeat(4,1fr);gap:10px;text-align:center">
    <div><div style="height:95px;background:linear-gradient(180deg,#d7dde3,#aab6c1)" role="img" aria-label="Team member portrait"></div><p class="h" style="margin-top:4px">Alex Moran</p><p class="p">Founder</p></div>
    <div><div style="height:95px;background:linear-gradient(180deg,#d7dde3,#aab6c1)" role="img" aria-label="Team member portrait"></div><p class="h" style="margin-top:4px">Dana Wu</p><p class="p">CTO</p></div>
    <div><div style="height:95px;background:linear-gradient(180deg,#d7dde3,#aab6c1)" role="img" aria-label="Team member portrait"></div><p class="h" style="margin-top:4px">Sam Ortiz</p><p class="p">Design</p></div>
    <div><div style="height:95px;background:linear-gradient(180deg,#d7dde3,#aab6c1)" role="img" aria-label="Team member portrait"></div><p class="h" style="margin-top:4px">Lee Park</p><p class="p">Sales</p></div>
  </div>
</section>

<section class="slide dark">
  <div class="ph ph-cyan" style="inset:0;opacity:.5" role="img" aria-label="Dark blue abstract technology backdrop"></div>
  <div class="center">
    <div class="logo" style="font-size:22px"><i style="width:20px;height:20px"></i>vxMender</div>
    <p style="margin:8px 0 0;font-size:12px;font-weight:600">Thank You</p>
    <p class="p w">For your attention</p>
  </div>
</section>

<section class="slide">
  <svg class="abs" style="right:0;top:0" width="230" height="214" viewBox="0 0 230 214"><polygon points="70,0 230,0 230,214 0,214" fill="#1ba9e1"/></svg>
  <div class="brand-sm" style="left:22px;right:auto;top:94px;font-size:12px"><i style="width:10px;height:10px"></i>vxMender</div>
  <div class="abs" style="right:26px;top:84px;color:var(--white);text-align:right">
    <p style="margin:0;font-size:16px;font-weight:600">Thank You</p>
    <p class="p w">Any questions are welcome</p>
  </div>
</section>

</main>
</body>
</html>
```